New Vegan Documentary Film Needs Poster Design

We are developing a documentary film production project called "Orchard Without Reckoning: A Quiet Weight Beneath Every Choice."

The documentary will explore the numerous consequences of our practice of commodifying animals for food. These consequences include:

* Cultural impact (global hunger, conflict and war, disease and health epidemics, waste.)
* Ecological toll (soil erosion, water &air pollution, rain forest devastation, global warming, species extinction, ocean destruction, etc.)
* Economic devastation (dependency on resources, health care & pharmaceutical/medical industry.)
Historical issues (cultural aggression, rise of the elite, slavery, domination of women.)
* Personal psyche (commodification of life, disconnectedness from and repression of our innate compassionate nature, intelligence, and sense of justice.)

The film will represent the ideals of kindness, justice, and freedom, and educate on the the keys to awakening from the invisible cultural food trance, and overall, be a vehicle to encourage awakening and living with awareness.

As per the film's title, we want the poster to convey the multi-layered global consequences of animal agriculture without openly attacking the meat industry or people eating animal-sourced foods.

This is a mass-appeal documentary intended to open the eyes of the general public without judgment or alienation of any sector of society. This is not about blame; it's about awareness. The poster should convey the same non-judgmental perspective.

Format should be standard film poster.
Copy for the poster must include the title, sub-title and a quote
Title: Orchard Without Reckoning:
Sub-title: A Quiet Weight Beneath Every Choice
Quote options (Pick one) -
As we sow, so shall we reap.
Question everything.
We are all in this together.
None of us is completely innocent.

```html
<!DOCTYPE html>
<html lang="en">
<head>
<meta charset="utf-8">
<title>Orchard Without Reckoning – Film Poster</title>
<link href="https://fonts.googleapis.com/css2?family=Cinzel:wght@600;700&family=Oswald:wght@300;400&display=swap" rel="stylesheet">
<style>
  :root {
    --sky: #e6ebef;
    --sky-mid: #c9d3da;
    --spray: #f4f7f8;
    --wave: #3c8e96;
    --wave-deep: #1b4a55;
    --street: #3a3632;
    --building: #c98a52;
    --city-dark: #16171b;
    --flare: #ff9a30;
    --title-box: rgba(40, 50, 62, 0.8);
    --title-ink: #ffffff;
    --title-edge: #c9a24a;
    --band: #f3ece2;
    --band-ink: #7a2a22;
    --quote-ink: #ffffff;
  }
  * { margin: 0; padding: 0; box-sizing: border-box; }
  html, body { width: 846px; height: 1200px; overflow: hidden; background: var(--city-dark); }
  .poster { position: relative; width: 846px; height: 1200px; overflow: hidden; }

  .poster-scene {
    position: absolute; inset: 0;
    background:
      radial-gradient(circle 70px at 560px 640px, rgba(255,230,170,0.9), rgba(255,154,48,0.5) 45%, transparent 100%),
      radial-gradient(circle 60px at 75px 650px, rgba(255,220,160,0.85), rgba(255,154,48,0.45) 45%, transparent 100%),
      radial-gradient(circle 90px at 560px 1010px, rgba(255,200,120,0.75), rgba(240,110,30,0.35) 50%, transparent 100%),
      radial-gradient(ellipse 140px 90px at 470px 340px, rgba(255,180,90,0.55), transparent 100%),
      radial-gradient(ellipse 360px 260px at 640px 1080px, rgba(200,80,40,0.35), transparent 100%),
      radial-gradient(ellipse 130px 110px at 720px 800px, rgba(220,150,90,0.75), transparent 100%),
      linear-gradient(90deg, transparent 0 600px, rgba(201,138,82,0.7) 620px 846px) 0 720px / 846px 180px no-repeat,
      radial-gradient(ellipse 360px 430px at 120px 960px, rgba(60,130,140,0.95), rgba(27,74,85,0.85) 55%, transparent 100%),
      radial-gradient(ellipse 300px 180px at 380px 800px, rgba(230,240,240,0.55), transparent 100%),
      radial-gradient(ellipse 620px 700px at -120px 420px, var(--wave-deep) 0 35%, var(--wave) 55%, rgba(190,220,222,0.9) 72%, transparent 86%),
      radial-gradient(ellipse 380px 260px at 240px 120px, var(--spray), transparent 100%),
      linear-gradient(180deg, var(--sky) 0%, var(--sky-mid) 40%, #7f7f80 60%, var(--street) 78%, var(--city-dark) 100%);
  }

  .title-block {
    position: absolute; left: 90px; top: 350px; width: 670px; height: 302px;
    background: var(--title-box);
    text-align: center; color: var(--title-ink);
  }
  .title-main {
    position: absolute; left: 0; right: 0; top: 0;
    font-family: "Cinzel", serif; font-weight: 700; font-size: 108px; line-height: 1;
    letter-spacing: -2px;
    text-shadow: -5px 4px 0 var(--title-edge);
  }
  .title-joiner {
    position: absolute; left: 30px; right: 15px; top: 120px; height: 40px;
    display: flex; align-items: center; gap: 14px;
  }
  .title-joiner::before, .title-joiner::after {
    content: ""; flex: 1; height: 3px; background: var(--title-ink);
  }
  .title-joiner span {
    font-family: "Cinzel", serif; font-weight: 600; font-size: 36px; line-height: 1;
    text-shadow: -3px 3px 0 var(--title-edge);
  }
  .title-accent {
    position: absolute; left: 0; right: 0; top: 118px;
    font-family: "Oswald", sans-serif; font-weight: 300; font-size: 176px; line-height: 1.1;
    letter-spacing: 1px;
    text-shadow: -4px 3px 0 rgba(201,162,74,0.8);
  }

  .subtitle-band {
    position: absolute; left: 18px; top: 672px; width: 770px; height: 46px;
  }
  .subtitle-band svg { position: absolute; inset: 0; }
  .subtitle-text {
    position: absolute; inset: 0;
    display: flex; align-items: center; justify-content: center;
    padding-left: 40px;
    font-family: "Cinzel", serif; font-weight: 700; font-size: 27px;
    color: var(--band-ink); letter-spacing: 0.3px; white-space: nowrap;
  }

  .tagline {
    position: absolute; right: 92px; top: 892px;
    font-family: "Oswald", sans-serif; font-weight: 300; font-size: 92px; line-height: 104px;
    color: var(--quote-ink); text-align: right; white-space: nowrap;
  }
  .tagline-rule {
    position: absolute; left: 770px; top: 910px; width: 2px; height: 215px;
    background: var(--quote-ink);
  }
</style>
</head>
<body>
<main class="poster">
  <div class="poster-scene" role="img" aria-label="A towering tsunami wave crashing over a city street, sweeping away buses and cars beside tall buildings, under a pale sky with warm light flares"></div>

  <header class="title-block">
    <h1>
      <span class="title-main">ORCHARD</span>
      <span class="title-joiner"><span>WITHOUT</span></span>
      <span class="title-accent">Reckoning</span>
    </h1>
  </header>

  <div class="subtitle-band">
    <svg width="770" height="46" viewBox="0 0 770 46" aria-hidden="true">
      <path d="M10 8 L760 4 L752 22 L766 40 L14 44 L0 26 Z" fill="var(--band)" opacity="0.92"/>
    </svg>
    <p class="subtitle-text">A QUIET WEIGHT BENEATH EVERY CHOICE</p>
  </div>

  <blockquote class="tagline">“as we sow,<br>so shall we reap”</blockquote>
  <div class="tagline-rule"></div>
</main>
</body>
</html>
```